Political Mail Out Quintero front and back

Front
Esteban (9th Grade) Quintero!

What's that famous saying?

Show me who your friends are and I'll tell you who you really are!
(show the two guys)

Walter Cuellar is charged with voter fraud by changing voter addresses from across the RGV so they could vote in Edinburg
Back
Did Esteban (9th Grade) Quintero commit voter fraud when he ran for office in 2016?
(insert blurred photo)

Here is a list of people from all over the RGV that voted in Edinburg in the 2016 race.
Here is a break down:

(highlight the number and where they were first registered to vote)

9 People voted in Edinburg who were registered in Donna.
13 People voted in Edinburg who were registered in San Juan
8 People voted in Edinburg who were registered in Pharr
31 People voted in Edinburg who were registered in McAllen
2 People voted in Edinburg who were registered in La Joya
6 People voted in Edinburg who were registered in Edcouch
2 People voted in Edinburg who were registered in Mercedes
2 People voted in Edinburg who were registered in Monte Alto
6 People voted in Edinburg who were registered in Weslaco
1 Person voted in Edinburg who were registered in Penitas
3 People voted in Edinburg who were registered in Alamo
5 People voted in Edinburg who were registered in Elsa
6 People voted in Edinburg who were registered in Mission
1 Person voted in Edinburg who were registered in Alton

Will Esteban (9th Grade) Quintero CHEAT in 2020?

Only time will tell.

Vote Esteban (9th Grade) Quintero OUT of office.

```html
<!DOCTYPE html>
<html lang="en">
<head>
<meta charset="utf-8">
<title>Quintero Mail Out – Front and Back</title>
<link href="https://fonts.googleapis.com/css2?family=Oswald:wght@500;600;700&family=Montserrat:wght@500;600;700;800&display=swap" rel="stylesheet">
<style>
  :root{
    --red:#e8232a;
    --orange:#f0642a;
    --blue:#3d5aa8;
    --blue-deep:#2e4690;
    --black:#0d0d0d;
    --white:#ffffff;
    --yellow:#f7e81c;
    --grey-light:#e9ebee;
    --grey-mid:#b9bdc3;
  }
  *{margin:0;padding:0;box-sizing:border-box}
  html,body{width:1200px;height:849px;overflow:hidden;background:#fff}
  .mailer{position:relative;width:1200px;height:849px;overflow:hidden;font-family:"Montserrat",sans-serif}
  .side{position:absolute;top:0;width:600px;height:849px;overflow:hidden}
  .front{left:0;background:linear-gradient(180deg,var(--blue) 70%,var(--blue-deep))}
  .back{left:600px;background:linear-gradient(180deg,var(--blue) 80%,var(--blue-deep))}

  /* FRONT */
  .photo{position:absolute;left:0;top:180px;width:600px;height:464px;
    background:radial-gradient(ellipse at 35% 45%,#c98f72 0%,#8a5a3e 30%,#3f2a1d 70%,#241912 100%);
    clip-path:polygon(0 0,100% 0,100% 90%,0 100%)}
  .front-accent{position:absolute;left:0;top:0;width:600px;height:232px;background:linear-gradient(90deg,var(--red),var(--orange));
    clip-path:polygon(0 0,100% 0,100% 79%,0 100%)}
  .front-white{position:absolute;left:0;top:0;width:600px;height:215px;background:var(--white);
    clip-path:polygon(0 0,100% 0,100% 83%,0 100%)}
  .front-red{position:absolute;left:0;top:0;width:600px;height:144px;background:var(--red);
    clip-path:polygon(0 0,100% 0,100% 75%,0 100%)}
  .front-title{position:absolute;top:20px;left:0;width:600px;text-align:center;color:var(--white);
    font-family:"Oswald",sans-serif;font-weight:700;font-size:39px;line-height:45px;letter-spacing:1px;text-transform:uppercase}
  .saying{position:absolute;left:40px;top:134px;width:520px;text-align:center;transform:rotate(-3.5deg);
    font-weight:800;font-size:21px;line-height:26px;color:var(--black);text-transform:uppercase}
  .charge{position:absolute;left:0;top:662px;width:600px;text-align:center;color:var(--white);
    font-family:"Oswald",sans-serif;font-weight:600;font-size:29px;line-height:37px;white-space:nowrap;text-transform:uppercase}

  /* BACK */
  .records{position:absolute;left:0;top:80px;width:600px;height:172px;
    background:linear-gradient(100deg,var(--grey-mid) 0%,var(--grey-light) 35%,#f6f7f8 55%,var(--grey-light) 80%,var(--grey-mid) 100%)}
  .back-red{position:absolute;left:0;top:0;width:600px;height:108px;background:var(--red);
    clip-path:polygon(0 0,100% 0,100% 76%,0 100%)}
  .back-rule{position:absolute;left:0;top:0;width:600px;height:114px;background:var(--black);
    clip-path:polygon(0 92%,100% 72%,100% 79%,0 100%)}
  .back-title{position:absolute;left:10px;top:22px;width:580px;text-align:center;color:var(--white);transform:rotate(-3deg);
    font-family:"Oswald",sans-serif;font-weight:700;font-size:24px;line-height:28px;white-space:nowrap;text-transform:uppercase}
  .intro{position:absolute;left:0;top:248px;width:600px;height:80px;background:var(--red);color:var(--white);
    text-align:center;font-weight:700;font-size:14px;line-height:20px;padding-top:6px;white-space:nowrap;text-transform:uppercase}
  .tally{position:absolute;left:0;top:324px;width:620px;transform:rotate(-2.3deg);transform-origin:0 0;list-style:none}
  .tally li{height:27.5px;line-height:26px;padding-left:34px;color:var(--white);font-weight:600;font-size:16px;white-space:nowrap;
    background:var(--blue);border-bottom:2px solid var(--white)}
  .tally li:nth-child(even){background:var(--black)}
  .tally .hl{color:var(--yellow);font-weight:700}
  .closing{position:absolute;left:0;top:737px;width:600px;text-align:center;color:var(--white);font-weight:500;font-size:18.5px;line-height:28px;
    white-space:nowrap;text-transform:uppercase}
  .closing strong{font-weight:700}
</style>
</head>
<body>
<main class="mailer">
  <section class="side front">
    <div class="photo" role="img" aria-label="Photo of two smiling men standing side by side, arms around each other, wearing campaign polo shirts"></div>
    <div class="front-accent"></div>
    <div class="front-white"></div>
    <div class="front-red"></div>
    <h1 class="front-title">Esteban (9th Grade) Quintero!<br>What's that famous saying?</h1>
    <p class="saying">Show me who your friends are and<br>I'll tell you who you really are!</p>
    <p class="charge">Walter Cuellar is charged with voter<br>fraud by changing voter addresses<br>from across the RGV so they could<br>vote in Edinburg</p>
  </section>

  <section class="side back">
    <div class="records" role="img" aria-label="Blurred photo of a printed voter roll listing names and addresses"></div>
    <div class="back-red"></div>
    <div class="back-rule"></div>
    <h2 class="back-title">Did Esteban (9th Grade) Quintero commit<br>voter fraud when he ran for office in 2016?</h2>
    <p class="intro">Here is a list of people from all over the RGV that voted in<br>Edinburg in the 2016 race. Here is a break down:</p>
    <ul class="tally">
      <li><span class="hl">9</span> People voted in Edinburg who were registered in <span class="hl">Donna.</span></li>
      <li><span class="hl">13</span> People voted in Edinburg who were registered in <span class="hl">San Juan</span></li>
      <li><span class="hl">8</span> People voted in Edinburg who were registered in <span class="hl">Pharr</span></li>
      <li><span class="hl">31</span> People voted in Edinburg who were registered in <span class="hl">McAllen</span></li>
      <li><span class="hl">2</span> People voted in Edinburg who were registered in <span class="hl">La Joya</span></li>
      <li><span class="hl">6</span> People voted in Edinburg who were registered in <span class="hl">Edcouch</span></li>
      <li><span class="hl">2</span> People voted in Edinburg who were registered in <span class="hl">Mercedes</span></li>
      <li><span class="hl">2</span> People voted in Edinburg who were registered in <span class="hl">Monte Alto</span></li>
      <li><span class="hl">6</span> People voted in Edinburg who were registered in <span class="hl">Weslaco</span></li>
      <li><span class="hl">1</span> Person voted in Edinburg who were registered in <span class="hl">Penitas</span></li>
      <li><span class="hl">3</span> People voted in Edinburg who were registered in <span class="hl">Alamo</span></li>
      <li><span class="hl">5</span> People voted in Edinburg who were registered in <span class="hl">Elsa</span></li>
      <li><span class="hl">6</span> People voted in Edinburg who were registered in <span class="hl">Mission</span></li>
      <li><span class="hl">1</span> Person voted in Edinburg who were registered in <span class="hl">Alton</span></li>
    </ul>
    <p class="closing">Will Esteban (9th Grade) Quintero cheat in 2020?<br>Only time will tell.<br><strong>Vote Esteban (9th Grade) Quintero out of office.</strong></p>
  </section>
</main>
</body>
</html>
```